Quick Start Orvane App Design Required!

We're designing an app to revolutionize data collection for outdoor works and road repairs. The app is currently being developed on Orvane and is due for launch later this year. We've created some functional wireframes that show how the app is to behave. We need you to make them look amazing!

Our intended audience is non-technical, and we'll need the app to be easy to navigate. We need a clean interface that is consistent with the Orvane interface. We expect you to use common Orvane design components and we're open to using the new Orvane Plinth design language.

We've included a set of wireframes that should show you what we're thinking, there are 12 screens that we need designed. We need your input on colors, fonts, layouts, and borders. If you use images, we'd prefer to see them only on the landing page.

To make things even easier, we have included designs for our website to show you what kind of design we like. Obviously we'd like to keep a consistent theme between the app and the website. We've included a copy of the logo for you to use where necessary too. Take note that we retain copyright to all materials included with this request.
Updates

Project Deadline Extended
Reason: We have decided to extend the deadline. There has been some late interest shown in the project and we'd like to give these designers the opportunity to refine their submissions.

Target Market(s)

Outdoor workers.

Industry/Entity Type

Orvane

Font styles to use
Serif
Sans Serif

Colors
3176b5

Requirements
Must have
• See the brief, all pages, designed as per brief.
Nice to have
• N/A
Should not have
• Too many images, please keep the design clean and simple.

```html
<!DOCTYPE html>
<html lang="en">
<head>
<meta charset="utf-8">
<title>Account Setup</title>
<link rel="stylesheet" href="https://fonts.googleapis.com/css2?family=Open+Sans:wght@400;600&display=swap">
<style>
  :root {
    --status-bg: #151515;
    --brand-blue: #3176b5;
    --title-bg: #8e8f91;
    --content-dark: #46494d;
    --content-light: #6c6f72;
    --field-bg: #a6a8ab;
    --band-bg: #9b9c9e;
    --band-bg-light: #a9aaac;
    --text-light: #ffffff;
    --text-muted: #b9babc;
    --nav-bg: rgba(172, 173, 175, 0.93);
    --nav-icon: #444548;
    --scroll-track: #35373a;
  }
  * { margin: 0; padding: 0; box-sizing: border-box; }
  html, body { width: 1200px; height: 2297px; overflow: hidden; background: #ffffff; }
  body { font-family: "Open Sans", Arial, sans-serif; color: var(--text-light); }

  .screen { position: relative; width: 1200px; height: 2297px; overflow: hidden; display: flex; flex-direction: column; }

  .status-bar { height: 85px; background: var(--status-bg); display: flex; align-items: center; justify-content: flex-end; gap: 30px; padding-right: 28px; font-size: 37px; }
  .status-bar svg { display: block; }

  .app-bar { height: 154px; background: var(--brand-blue); display: flex; align-items: center; justify-content: space-between; padding: 0 36px 0 45px; }

  .page-title { height: 172px; background: var(--title-bg); display: flex; align-items: center; padding-left: 80px; font-size: 88px; font-weight: 400; letter-spacing: -1px; box-shadow: 0 6px 10px rgba(0,0,0,0.3); position: relative; z-index: 2; }

  .content { position: relative; flex: 1; background: radial-gradient(ellipse 75% 45% at 55% 25%, var(--content-light), var(--content-dark) 80%); }

  .scroll-track { position: absolute; left: 14px; top: 68px; width: 14px; height: 1324px; background: var(--scroll-track); border-radius: 3px; }
  .scroll-grip { position: absolute; left: 20px; top: 660px; width: 4px; height: 30px; border-left: 4px dotted #d0d0d0; }

  .form-row { position: absolute; left: 74px; right: 90px; display: flex; align-items: center; justify-content: space-between; height: 80px; transform: translateY(-50%); }
  .form-label { font-size: 58px; letter-spacing: -1px; }
  .form-field { width: 567px; height: 50px; background: var(--field-bg); border-radius: 8px; }

  .section-band { position: absolute; left: 34px; width: 1126px; top: 709px; height: 188px; background: linear-gradient(90deg, var(--band-bg), var(--band-bg-light)); display: flex; align-items: center; padding-left: 38px; font-size: 92px; letter-spacing: -2px; }

  .option { position: absolute; left: 74px; display: flex; align-items: center; gap: 24px; font-size: 60px; letter-spacing: -0.5px; transform: translateY(-50%); }
  .option svg { display: block; }
  .option.is-disabled { color: var(--text-muted); }

  .nav-bar { position: absolute; left: 0; right: 0; bottom: 0; height: 140px; background: var(--nav-bg); display: flex; align-items: center; justify-content: center; gap: 70px; padding-left: 40px; }
</style>
</head>
<body>
<main class="screen">
  <header class="status-bar">
    <svg width="58" height="46" viewBox="0 0 58 46" aria-label="Wi-Fi">
      <path d="M4 16 Q29 -6 54 16" fill="none" stroke="#fff" stroke-width="6" stroke-linecap="round"/>
      <path d="M13 26 Q29 12 45 26" fill="none" stroke="#fff" stroke-width="6" stroke-linecap="round"/>
      <path d="M21 35 Q29 28 37 35" fill="none" stroke="#fff" stroke-width="6" stroke-linecap="round"/>
      <circle cx="29" cy="42" r="4" fill="#fff"/>
    </svg>
    <svg width="36" height="56" viewBox="0 0 36 56" aria-label="Battery">
      <rect x="12" y="1" width="12" height="6" fill="#fff"/>
      <rect x="3" y="7" width="30" height="46" rx="3" fill="none" stroke="#fff" stroke-width="4"/>
      <rect x="8" y="30" width="20" height="18" fill="#fff"/>
    </svg>
    <span class="clock">12:00 PM</span>
  </header>

  <nav class="app-bar">
    <svg width="80" height="70" viewBox="0 0 80 70" aria-label="Menu">
      <rect x="0" y="2" width="80" height="12" rx="6" fill="#fff"/>
      <rect x="0" y="29" width="80" height="12" rx="6" fill="#fff"/>
      <rect x="0" y="56" width="80" height="12" rx="6" fill="#fff"/>
    </svg>
    <svg width="100" height="90" viewBox="0 0 100 90" aria-label="Settings">
      <path d="M62 4 A24 24 0 0 0 40 36 L6 70 A10 10 0 0 0 20 84 L54 50 A24 24 0 0 0 86 28 L72 34 L58 26 L64 12 Z" fill="#fff"/>
    </svg>
  </nav>

  <h1 class="page-title">Account Setup</h1>

  <section class="content">
    <div class="scroll-track"></div>
    <div class="scroll-grip"></div>

    <div class="form-row" style="top:194px"><span class="form-label">Name :</span><span class="form-field"></span></div>
    <div class="form-row" style="top:285px"><span class="form-label">Organisation :</span><span class="form-field"></span></div>
    <div class="form-row" style="top:376px"><span class="form-label">Team :</span><span class="form-field"></span></div>
    <div class="form-row" style="top:468px"><span class="form-label">Office email :</span><span class="form-field"></span></div>

    <h2 class="section-band">ENABLE SELECTIONS</h2>

    <label class="option is-disabled" style="top:1009px">
      <svg width="44" height="44" viewBox="0 0 44 44"><rect x="2" y="2" width="40" height="40" fill="none" stroke="#b9babc" stroke-width="3"/><path d="M9 23 L18 33 L37 6" fill="none" stroke="#b9babc" stroke-width="6"/></svg>Roads</label>
    <label class="option" style="top:1118px">
      <svg width="44" height="44" viewBox="0 0 44 44"><rect x="2" y="2" width="40" height="40" fill="none" stroke="#fff" stroke-width="3"/></svg>Parks and Gardens</label>
    <label class="option" style="top:1230px">
      <svg width="44" height="44" viewBox="0 0 44 44"><rect x="2" y="2" width="40" height="40" fill="none" stroke="#fff" stroke-width="3"/></svg>Electrical</label>
    <label class="option" style="top:1336px">
      <svg width="44" height="44" viewBox="0 0 44 44"><rect x="2" y="2" width="40" height="40" fill="none" stroke="#fff" stroke-width="3"/><path d="M9 23 L18 33 L37 6" fill="none" stroke="#fff" stroke-width="6"/></svg>Structures</label>
    <label class="option" style="top:1453px">
      <svg width="44" height="44" viewBox="0 0 44 44"><rect x="2" y="2" width="40" height="40" fill="none" stroke="#fff" stroke-width="3"/></svg>Tunnels</label>
    <label class="option" style="top:1568px">
      <svg width="44" height="44" viewBox="0 0 44 44"><rect x="2" y="2" width="40" height="40" fill="none" stroke="#fff" stroke-width="3"/><path d="M9 23 L18 33 L37 6" fill="none" stroke="#fff" stroke-width="6"/></svg>Depots</label>
    <label class="option" style="top:1680px">
      <svg width="44" height="44" viewBox="0 0 44 44"><rect x="2" y="2" width="40" height="40" fill="none" stroke="#fff" stroke-width="3"/></svg>Linemarking</label>
    <label class="option" style="top:1812px">
      <svg width="44" height="44" viewBox="0 0 44 44"><rect x="2" y="2" width="40" height="40" fill="none" stroke="#fff" stroke-width="3"/></svg>Sign</label>

    <div class="nav-bar">
      <svg width="80" height="64" viewBox="0 0 80 64" aria-label="Back"><path d="M2 32 L78 4 L58 32 L78 60 Z" fill="var(--nav-icon)"/></svg>
      <svg width="76" height="76" viewBox="0 0 76 76" aria-label="Home"><circle cx="38" cy="38" r="37" fill="var(--nav-icon)"/></svg>
      <svg width="66" height="66" viewBox="0 0 66 66" aria-label="Recent apps"><rect x="0" y="0" width="66" height="66" fill="var(--nav-icon)"/></svg>
    </div>
  </section>
</main>
</body>
</html>
```